new business card and logo for a high end Automotive repair and performance shop

Need to update our design for our business cards. New address, and want a new look. I'll upload some pics of our current card. We are a high end auto repair/tuning shop. New address will be 5192 W. Larkfield Ave Brookvale, T.X. 70419. I do have the vector files if needed. The logo would have a similar design. Love the look of carbon fiber, and brushed aluminum, although may have issues showing the texture of the material due to dpi restrictions during card printing. Also the logo would have to be easily printed on shirts, and for embroidery. Thanks, and good luck.

www.motor-zenith.example

Target Market(s)

High end automotive repair, dealership alternative.

Industry/Entity Type

Automotive

Contact Information for Business Card

MOTORZENITH
5192 W. LARKFIELD AVE
BROOKVALE, T.X. 70419
PH 555-307-9261
FAX 555-307-4470
EMAIL INFO@MOTOR-ZENITH.EXAMPLE

Logo Text

MotorZenith

Font styles to use
Sans Serif

Requirements
Must have
• name, address, description that was uploaded.
Nice to have
• maybe some brands i.e. vardo, orvex, Talvani, qrt, solvanta, dovik etc. not necessary. simple is good, like the look of carbon fiber, brushed aluminum.
Should not have
• open to all suggestions.

```html
<!DOCTYPE html>
<html lang="en">
<head>
<meta charset="utf-8">
<title>MotorZenith Business Card</title>
<link rel="stylesheet" href="https://fonts.googleapis.com/css2?family=Arimo:wght@400;700&family=Lato:wght@400;700&family=Courier+Prime:wght@700&family=Archivo+Black&display=swap">
<style>
  :root {
    --page: #2a2a2a;
    --card-dark: #1b1b1b;
    --card-dark-2: #2c2c2c;
    --card-light: #ffffff;
    --card-light-2: #ececec;
    --accent: #e0141b;
    --ink: #1a1a1a;
    --silver: #c9c9c9;
    --muted: #b5b5b5;
  }
  * { box-sizing: border-box; margin: 0; padding: 0; }
  html, body { width: 1200px; height: 997px; overflow: hidden; }
  body { background: var(--page); position: relative; font-family: "Arimo", Arial, sans-serif; }

  .card {
    position: absolute;
    width: 560px;
    height: 320px;
    overflow: hidden;
    box-shadow: 0 14px 30px rgba(0,0,0,.55);
  }

  /* Front */
  .card--front { left: 80px; top: 110px; background: var(--card-dark); }
  .front__top {
    position: absolute; left: 0; top: 0; width: 100%; height: 160px;
    background: linear-gradient(180deg, var(--card-light), var(--card-light-2));
    display: flex; align-items: center; justify-content: center;
  }
  .front__rule {
    position: absolute; left: 0; top: 160px; width: 100%; height: 3px; background: var(--accent);
  }
  .front__notch {
    position: absolute; left: 40px; top: 161px;
    width: 0; height: 0;
    border-left: 9px solid transparent; border-right: 9px solid transparent;
    border-top: 9px solid var(--accent);
  }
  .front__bottom-rule {
    position: absolute; left: 0; bottom: 10px; width: 100%; height: 2px; background: var(--accent);
  }
  .front__body {
    position: absolute; left: 0; top: 163px; width: 100%; bottom: 12px;
    background: linear-gradient(180deg, var(--card-dark-2), var(--card-dark));
  }
  .person { position: absolute; left: 36px; top: 18px; }
  .person__name { color: var(--accent); font-size: 19px; line-height: 1.2; }
  .person__role { color: var(--muted); font-size: 13px; margin-top: 2px; }
  .contact-list { list-style: none; margin-top: 12px; }
  .contact-list li {
    color: var(--muted); font-size: 13px; line-height: 16px;
    display: flex; align-items: center; gap: 10px; margin-bottom: 4px;
  }
  .contact-list svg { width: 10px; height: 10px; fill: var(--accent); flex: none; }
  .company { position: absolute; right: 30px; top: 20px; text-align: right; }
  .company__name { color: var(--accent); font-size: 14px; letter-spacing: .5px; }
  .company__address { color: var(--muted); font-size: 12px; line-height: 1.4; margin-top: 4px; }

  .brand { display: flex; align-items: center; gap: 10px; }
  .brand__mark { width: 22px; height: 22px; background: var(--accent); }
  .brand__name { font-family: "Lato", sans-serif; font-weight: 700; letter-spacing: 3px; }
  .card--front .brand__name { color: var(--ink); font-size: 28px; }

  /* Back */
  .card--back { left: 560px; top: 540px; }
  .back__texture {
    position: absolute; inset: 0;
    background: radial-gradient(ellipse at 45% 35%, #3a3a3a 0%, #1e1e1e 60%, #121212 100%);
  }
  .back__content {
    position: absolute; inset: 0; display: flex; flex-direction: column; align-items: center; padding-top: 78px;
  }
  .card--back .brand__name { color: var(--silver); font-size: 32px; }
  .back__url {
    font-family: "Courier Prime", monospace; font-weight: 700; color: var(--accent);
    font-size: 16px; margin-top: 34px; letter-spacing: 1px;
  }
  .back__tagline {
    font-family: "Lato", sans-serif; color: var(--muted); font-size: 14px; text-align: center;
    line-height: 1.55; margin-top: 30px; letter-spacing: .4px; padding: 0 24px;
  }

  .caption {
    position: absolute; left: 735px; top: 895px;
    font-family: "Archivo Black", sans-serif; color: var(--accent); font-size: 28px; letter-spacing: 3px;
  }
</style>
</head>
<body>

<section class="card card--front" aria-label="Business card front">
  <div class="front__top">
    <div class="brand">
      <span class="brand__mark"></span>
      <span class="brand__name">MOTORZENITH</span>
    </div>
  </div>
  <div class="front__body">
    <div class="person">
      <p class="person__name">Dan Pierce</p>
      <p class="person__role">Owner</p>
      <ul class="contact-list">
        <li><svg viewBox="0 0 10 10"><path d="M2 0h2l1 2.5-1.3 1A5 5 0 0 0 6.5 6.3l1-1.3L10 6v2a2 2 0 0 1-2 2A8 8 0 0 1 0 2a2 2 0 0 1 2-2z"/></svg>555-307-9261</li>
        <li><svg viewBox="0 0 10 10"><rect x="1" y="2" width="8" height="7"/><rect x="3" y="0" width="4" height="3"/></svg>555-307-4470</li>
        <li><svg viewBox="0 0 10 10"><rect x="0" y="2" width="10" height="7"/></svg>info@motor-zenith.example</li>
      </ul>
    </div>
    <div class="company">
      <p class="company__name">MOTORZENITH</p>
      <p class="company__address">5192 W. Larkfield Ave<br>Brookvale, T.X. 70419</p>
    </div>
  </div>
  <div class="front__rule"></div>
  <div class="front__notch"></div>
  <div class="front__bottom-rule"></div>
</section>

<section class="card card--back" aria-label="Business card back">
  <div class="back__texture" role="img" aria-label="Carbon fiber texture background"></div>
  <div class="back__content">
    <div class="brand">
      <span class="brand__mark"></span>
      <span class="brand__name">MOTORZENITH</span>
    </div>
    <p class="back__url">http://www.motor-zenith.example/</p>
    <p class="back__tagline">SPECIALIZING IN ASIAN, EUROPEAN &amp; DOMESTIC VECHICLE REPAIR,<br>SERVICE , FABRICATION &amp; PREFORMANCE.</p>
  </div>
</section>

<p class="caption">In carbon fiber look</p>

</body>
</html>
```